Copper lark buildworks

Copper lark buildworks is a small construction company.
Who is a licenced builder, Carpenter, joiner,
working on heritage ,new build, speacial projects and sometimes furniture

Industry/Entity Type

Construction

```html
<!DOCTYPE html>
<html lang="en">
<head>
<meta charset="UTF-8">
<title>Copper lark buildworks – Business Card</title>
<link rel="stylesheet" href="https://fonts.googleapis.com/css2?family=Open+Sans:wght@400;600;700&display=swap">
<style>
  :root {
    --page-bg: #e9e6e1;
    --card-light: #eef0ef;
    --card-dark: #1b1b1b;
    --ink: #222222;
    --ink-soft: #3a3a3a;
    --green-bright: #7ed321;
    --green-mid: #5aae1f;
    --green-deep: #2f7d1a;
    --white: #ffffff;
    --icon-bg: #ffffff;
    --icon-ink: #1b1b1b;
  }
  * { box-sizing: border-box; margin: 0; padding: 0; }
  html, body {
    width: 1200px;
    height: 960px;
    overflow: hidden;
    background: var(--page-bg);
    font-family: "Open Sans", Arial, sans-serif;
  }
  .canvas {
    position: relative;
    width: 1200px;
    height: 960px;
  }
  .business-card {
    position: absolute;
    left: 100px;
    top: 170px;
    width: 1000px;
    height: 620px;
    display: flex;
    box-shadow: 0 14px 34px rgba(0, 0, 0, 0.28);
  }

  /* Front / identity side */
  .identity-side {
    position: relative;
    width: 500px;
    height: 100%;
    background: var(--card-light);
    overflow: hidden;
  }
  .brand {
    position: absolute;
    left: 84px;
    top: 62px;
    display: flex;
    align-items: center;
    gap: 18px;
  }
  .brand-dot {
    width: 34px;
    height: 34px;
    border-radius: 50%;
    background: var(--green-bright);
    flex: none;
  }
  .brand-name {
    color: var(--ink);
    font-weight: 700;
    font-size: 58px;
    line-height: 1.02;
    letter-spacing: -0.5px;
  }
  .person {
    position: absolute;
    left: 84px;
    top: 300px;
    width: 340px;
  }
  .person-name {
    font-size: 52px;
    font-weight: 400;
    color: var(--ink);
    line-height: 1.1;
    white-space: nowrap;
  }
  .person-name .initial { color: var(--green-bright); }
  .person-role {
    margin-top: 6px;
    text-align: right;
    font-size: 22px;
    font-weight: 600;
    color: var(--ink-soft);
  }
  .city-band {
    position: absolute;
    left: 0;
    bottom: 0;
    width: 500px;
    height: 150px;
    background: linear-gradient(90deg, var(--green-deep) 0%, var(--green-mid) 55%, var(--green-bright) 100%);
  }

  /* Back / contact side */
  .contact-side {
    position: relative;
    width: 500px;
    height: 100%;
    background: var(--card-dark);
    color: var(--white);
  }
  .contact-list {
    list-style: none;
    position: absolute;
    left: 56px;
    top: 100px;
  }
  .contact-item {
    display: flex;
    align-items: center;
    gap: 26px;
    height: 48px;
    margin-bottom: 28px;
    font-size: 25px;
    font-weight: 400;
  }
  .contact-icon {
    width: 40px;
    height: 40px;
    flex: none;
  }
  .service-list {
    list-style: none;
    position: absolute;
    left: 56px;
    top: 486px;
    display: grid;
    grid-template-columns: 212px 200px;
    row-gap: 16px;
  }
  .service-item {
    display: flex;
    align-items: center;
    gap: 14px;
    font-size: 19px;
  }
  .service-leaf {
    width: 22px;
    height: 16px;
    flex: none;
  }
</style>
</head>
<body>
<main class="canvas">
  <article class="business-card">
    <section class="identity-side">
      <div class="brand">
        <span class="brand-dot"></span>
        <h1 class="brand-name">Copper lark<br>buildworks</h1>
      </div>
      <div class="person">
        <p class="person-name"><span class="initial">M</span>arcus <span class="initial">H</span>ale</p>
        <p class="person-role">Directer</p>
      </div>
      <div class="city-band" role="img" aria-label="Green city skyline silhouette along the bottom edge"></div>
    </section>

    <section class="contact-side">
      <ul class="contact-list">
        <li class="contact-item">
          <svg class="contact-icon" viewBox="0 0 40 40" aria-hidden="true">
            <circle cx="20" cy="20" r="20" fill="var(--icon-bg)"/>
            <path d="M14 11c1.2-0.6 2.3 0 3 1.4l1.4 2.8c0.5 1 0.2 2-0.7 2.6l-1 0.7c0.9 2.2 2.6 3.9 4.8 4.8l0.7-1c0.6-0.9 1.6-1.2 2.6-0.7l2.8 1.4c1.4 0.7 2 1.8 1.4 3-1 2-3 3-5 2.5-5.6-1.5-10-5.9-11.5-11.5-0.5-2 0.5-4 2.5-5z" fill="var(--icon-ink)"/>
          </svg>
          <span>0491570236</span>
        </li>
        <li class="contact-item">
          <svg class="contact-icon" viewBox="0 0 40 40" aria-hidden="true">
            <circle cx="20" cy="20" r="20" fill="var(--icon-bg)"/>
            <circle cx="20" cy="20" r="10" fill="none" stroke="var(--icon-ink)" stroke-width="2.2"/>
            <ellipse cx="20" cy="20" rx="4.5" ry="10" fill="none" stroke="var(--icon-ink)" stroke-width="2"/>
            <line x1="10" y1="20" x2="30" y2="20" stroke="var(--icon-ink)" stroke-width="2"/>
          </svg>
          <span>www.copperlarkbuild.com</span>
        </li>
        <li class="contact-item">
          <svg class="contact-icon" viewBox="0 0 40 40" aria-hidden="true">
            <circle cx="20" cy="20" r="20" fill="var(--icon-bg)"/>
            <rect x="10" y="13" width="20" height="14" rx="1.5" fill="var(--icon-ink)"/>
            <path d="M10.5 14l9.5 7 9.5-7" fill="none" stroke="var(--icon-bg)" stroke-width="1.8"/>
          </svg>
          <span>hello@copperlarkbuild.com</span>
        </li>
        <li class="contact-item">
          <svg class="contact-icon" viewBox="0 0 40 40" aria-hidden="true">
            <circle cx="20" cy="20" r="19" fill="var(--card-dark)" stroke="#3c3c3c" stroke-width="2"/>
            <path d="M20 10c-4 0-7 3-7 6.8 0 5 7 13.2 7 13.2s7-8.2 7-13.2C27 13 24 10 20 10z" fill="var(--white)"/>
            <circle cx="20" cy="17" r="2.6" fill="var(--card-dark)"/>
          </svg>
          <span>18 Tanner Street.</span>
        </li>
      </ul>

      <ul class="service-list">
        <li class="service-item">
          <svg class="service-leaf" viewBox="0 0 22 16" aria-hidden="true"><path d="M1 15C3 4 11 1 21 1 20 11 13 15 1 15z" fill="var(--green-bright)"/></svg>
          <span>Licenced Builder</span>
        </li>
        <li class="service-item">
          <svg class="service-leaf" viewBox="0 0 22 16" aria-hidden="true"><path d="M1 15C3 4 11 1 21 1 20 11 13 15 1 15z" fill="var(--green-bright)"/></svg>
          <span>Speacial projects</span>
        </li>
        <li class="service-item">
          <svg class="service-leaf" viewBox="0 0 22 16" aria-hidden="true"><path d="M1 15C3 4 11 1 21 1 20 11 13 15 1 15z" fill="var(--green-bright)"/></svg>
          <span>Joiner</span>
        </li>
        <li class="service-item">
          <svg class="service-leaf" viewBox="0 0 22 16" aria-hidden="true"><path d="M1 15C3 4 11 1 21 1 20 11 13 15 1 15z" fill="var(--green-bright)"/></svg>
          <span>New build</span>
        </li>
      </ul>
    </section>
  </article>
</main>
</body>
</html>
```